International Marketing Company - Web Design Project

kVesta is a well-funded start up in London developing an Online Marketing Platform for small businesses in Europe.

We require a large number of high quality business web designs for our business website builder. Our business websites are completely integrated into our Online Marketing systems and therefore it is important for designers to comply with our Design Guidelines.

This initial contest is a trial for us to open up the design process to top designers for the Builders vertical (e.g. Builders, Electricians, Plumbers, Flooring, etc.). We have implemented a base html structure and design and included them in the files.

Use your creativity to design new and fresh designs based on the included elements (e.g. testimonials, business description, etc).

We will award the stated prize money for the top three designs.

Any designers that submit designs we feel are of a high enough quality but do not make the top 3 could still be compensated and WILL be invited to participate in our next vertical competition.

Therefore, we encourage designers to submit as many designs as possible as we may award up to 25 designs.

Submissions will be reviewed daily and feedback provided where possible.

Designers who can also code will have the options to implement their designs for an additional fee.

Good luck!
Updates

There has been a mistake made in regard to the prize. Pixel Harbor should have it fixed soon.

1st place = £350
2nd place = £250
3rd Place = £150

Thanks,
Dorian
25/11/2011

UPDATE:

1st place will win £350
2nd place will win £250
3rd place will win £150

Everything else is as to the specification.

Thanks
Dorian

Target Market(s)

Builders, Electricians, Plumbers, Tradesman, Small construction companies

Industry/Entity Type

Business

Requirements
Must have
• Totally new designs based around the elements we want to show on each page.

We are looking for something different to the design we already have. But you can use that as a starting point.

Use the included files to see what is required for each page. Here is a brief outline:

Homepage - Testimonials, News, Business Description, Latest Projects and Call to action

About-Us - Team Summary, About the Business and a call to action

Projects Page - Project Details (Oage Title and description), Each project needs a title, content and 2 images.

Testimonials Page - The testifiers name and their comment

Contacts Page - Trovix Map, Company address, business hours, contact form and a call to action.

Please submit final designs in Photoshop or Fireworks format.

Each page has a set of elements. These element must feature in the design of that page. See supporting documents for page details.

All elements must be included in your design. Please do not add any extra element.

Professional look and feel
Nice to have
• Design variations:
Full width designs
Boxed Designs
With AND without carousels
OR static images
Good use of stock images.

Creative use of the elements, dont be restricted/influenced by the default design we have already

Designs based on the 960 grid

```html
<!DOCTYPE html>
<html lang="en">
<head>
<meta charset="utf-8">
<title>Ridgeway Builders – Gallery</title>
<link rel="stylesheet" href="https://fonts.googleapis.com/css2?family=Arimo:ital,wght@0,400;0,700;1,400&family=Noto+Sans:wght@400;700&display=swap">
<style>
  :root {
    --ink: #111111;
    --text: #222222;
    --muted: #6f6f6f;
    --accent: #f2cf1e;
    --nav-top: #3a3a3a;
    --nav-bottom: #050505;
    --panel-top: #8a8a8a;
    --panel-bottom: #585858;
    --frame: #e2e2e2;
    --rule: #ebebeb;
    --white: #ffffff;
  }
  * { margin: 0; padding: 0; box-sizing: border-box; }
  html, body { width: 1200px; height: 900px; overflow: hidden; background: var(--white); }
  body { position: relative; font-family: "Noto Sans", Tahoma, sans-serif; color: var(--text); }
  .abs { position: absolute; }

  .brand { left: 122px; top: 20px; display: flex; align-items: center; gap: 8px; white-space: nowrap;
    font: 700 26px/1 "Arimo", Arial, sans-serif; color: var(--ink); }
  .brand-dot { width: 16px; height: 16px; border-radius: 50%; background: var(--accent); }

  .main-nav { left: 120px; top: 53px; width: 960px; height: 43px;
    background: linear-gradient(var(--nav-top), var(--nav-bottom)); }
  .main-nav ul { list-style: none; display: flex; gap: 16px; position: absolute; left: 34px; top: 13px;
    font: 400 18px/1 "Arimo", Arial, sans-serif; color: var(--white); white-space: nowrap; }
  .nav-call { position: absolute; right: 35px; top: 12px; display: flex; align-items: center; gap: 10px;
    font: 400 20px/1 "Arimo", Arial, sans-serif; color: var(--white); white-space: nowrap; }

  .hero { left: 120px; top: 96px; width: 960px; height: 267px; overflow: hidden;
    background: linear-gradient(100deg, #c9926a 0%, #8a5a3a 30%, #5f5c58 50%, #9a6c4c 75%, #c08a62 100%); }
  .hero-caption { position: absolute; left: 550px; top: 97px; width: 410px; height: 170px;
    background: rgba(90,90,90,0.7); }
  .hero-title { position: absolute; right: 57px; top: 42px; white-space: nowrap;
    font: italic 400 58px/1 "Arimo", Arial, sans-serif; color: var(--white); }
  .hero-tagline { position: absolute; right: 59px; top: 102px; white-space: nowrap;
    font: 400 38px/1 "Arimo", Arial, sans-serif; color: var(--white); }

  .section-title { font: 700 20px/1 "Arimo", Arial, sans-serif; color: var(--ink); white-space: nowrap; }
  .title-bar { height: 5px; }
  .intro { left: 122px; top: 421px; width: 680px; font-size: 13px; line-height: 18px; color: var(--text); }

  .cta { left: 813px; top: 396px; width: 265px; height: 112px; text-align: center;
    background: linear-gradient(var(--panel-top), var(--panel-bottom)); }
  .cta-lead { margin-top: 24px; font: 400 19px/1 "Noto Sans", sans-serif; color: var(--white); white-space: nowrap; }
  .cta-action { margin-top: 6px; display: flex; justify-content: center; align-items: center; gap: 6px;
    font: 700 26px/1 "Noto Sans", sans-serif; color: var(--accent); white-space: nowrap; }

  .category-text { left: 128px; top: 592px; width: 286px; font: 400 14px/17px "Arimo", Arial, sans-serif; color: var(--muted); }

  .project { width: 207px; }
  .project-frame { width: 207px; height: 156px; border: 1px solid var(--frame); background: #f6f6f6; padding: 5px;
    box-shadow: 0 10px 8px -8px rgba(0,0,0,0.35); }
  .project-image { width: 195px; height: 144px;
    background: linear-gradient(160deg, #f2f0ea 0%, #d9cbb0 40%, #b48a55 60%, #e6e4de 100%); }
  .project-caption { margin-top: 20px; text-align: center; white-space: nowrap;
    font: 400 14px/1 "Noto Sans", sans-serif; color: var(--muted); }

  .footer-rule { left: 120px; top: 852px; width: 960px; height: 5px; background: var(--rule); }
  .footer-links, .copyright { top: 866px; font: 400 12px/1 "Noto Sans", sans-serif; color: var(--muted); white-space: nowrap; }
  .footer-links { left: 120px; }
  .copyright { right: 120px; }
</style>
</head>
<body>
  <header>
    <div class="abs brand"><span class="brand-dot"></span>Ridgeway Builders</div>
    <nav class="abs main-nav">
      <ul><li>Home</li><li>About</li><li>Testimonials</li><li>Portfolio</li><li>Contacts</li></ul>
      <div class="nav-call">
        <svg width="17" height="17" viewBox="0 0 17 17" aria-hidden="true">
          <rect width="17" height="17" rx="2" fill="#fff"/>
          <path d="M5 3.5c-1 .6-1.5 1.8-1 3.3.9 2.8 3.3 5.6 6 6.6 1.4.5 2.6 0 3.2-1l-2-1.8-1.3.9c-1.4-.7-2.6-2-3.3-3.4l.9-1.3z" fill="#111"/>
        </svg>
        Call : 020. 4821 7390
      </div>
    </nav>
    <div class="abs hero" role="img" aria-label="Photo of a builder in a hard hat working inside a timber house frame">
      <div class="hero-caption">
        <div class="hero-title">RIDGEWAY</div>
        <div class="hero-tagline">Quick . Solid . Quality</div>
      </div>
    </div>
  </header>

  <main>
    <h1 class="abs section-title" style="left:123px;top:381px;">Gallery</h1>
    <div class="abs title-bar" style="left:122px;top:402px;width:359px;background:var(--ink);"></div>
    <p class="abs intro">A short description about the projects page could go here. Attention to detail and our passion for presenta&shy;tion reside in every facet of our proecess from planning, budget compilation, project execution and sub-contractor selection.ur proecess from planning, budget compilation, project execution and sub-contractor selection.</p>

    <a class="abs cta">
      <div class="cta-lead">For more information</div>
      <div class="cta-action">
        <svg width="34" height="22" viewBox="0 0 34 22" aria-hidden="true">
          <path d="M0 0h8l11 11-11 11H0l11-11z M14 0h8l11 11-11 11h-8l11-11z" fill="#f2cf1e"/>
        </svg>
        Contact Us!
      </div>
    </a>

    <h2 class="abs section-title" style="left:124px;top:545px;">Residential: Kitchens</h2>
    <div class="abs title-bar" style="left:124px;top:565px;width:488px;background:var(--accent);"></div>
    <p class="abs category-text">Attention to detail and our passion for presen&shy;tation reside in every facet of our proecess from planning, budget compilation, project execution and sub-contractor selection.Attention to detail and our passion for presentation reside in every facet of our proecess from planning, budget compilation, project execution and sub-contractor selec&shy;tion.</p>

    <figure class="abs project" style="left:443px;top:596px;">
      <div class="project-frame"><div class="project-image" role="img" aria-label="Photo of a restored kitchen with wooden cabinets and tiled floor"></div></div>
      <figcaption class="project-caption">House restoration in Crawley</figcaption>
    </figure>
    <figure class="abs project" style="left:660px;top:596px;">
      <div class="project-frame"><div class="project-image" role="img" aria-label="Photo of a restored kitchen with wooden cabinets and tiled floor"></div></div>
      <figcaption class="project-caption">House restoration in Crawley</figcaption>
    </figure>
    <figure class="abs project" style="left:876px;top:596px;">
      <div class="project-frame"><div class="project-image" role="img" aria-label="Photo of a restored kitchen with wooden cabinets and tiled floor"></div></div>
      <figcaption class="project-caption">House restoration in Crawley</figcaption>
    </figure>
  </main>

  <footer>
    <div class="abs footer-rule"></div>
    <div class="abs footer-links">Home | About Us | Testimoniasl | Portfolio | Contact</div>
    <div class="abs copyright">© Copyright 2011 - Ridgeway Builders</div>
  </footer>
</body>
</html>
```